Letterhead Design for Vostrana Corporate Stationery

We are seeking a talented designer on ArtHarbor to create a professional and cohesive corporate stationery set for our company, Vostrana. Vostrana is a prominent player in the Commercial Real Estate industry, and we need stationery that reflects our brand's excellence and professionalism.

Scope of Work:

1. Letterhead Template (Microsoft Word):

Design a letterhead template in Microsoft Word format that adheres to our brand standards (attached in project files).
Include all necessary elements such as company logo, address, contact information, and any other relevant details.
The letterhead should be clean, elegant, and suitable for official business correspondence.

2. Business Cards:

Design business cards for our team members using the provided brand guidelines.
Include name, title, contact information, and the Vostrana logo.
Create a design that leaves a lasting impression and reflects our brand's professionalism.

3. Envelopes:

Design envelopes in various sizes (e.g., standard letter and legal sizes) that match the overall stationery theme.
Ensure that the design includes our company name, logo, and return address in accordance with brand guidelines.

4. Stationery:

Create a visually appealing stationery template that can be used for various documents and correspondence.
Ensure that the stationery design aligns with our brand standards and maintains consistency across all materials.

Submission Requirements:

Provide high-resolution files for each item (letterhead, business cards, envelopes, and stationery) in formats suitable for both print and digital use.
Include editable source files (e.g., Adobe Illustrator, Photoshop) for future modifications if necessary.

Design Guidelines:

Our brand is known for professionalism, trustworthiness, and excellence in the Commercial Real Estate industry. Please adhere to the brand standards provided in the project attachments.
Use our company colors, fonts, and logo as specified in the brand guidelines.
Feel free to be creative within the boundaries of our brand to make our stationery stand out while maintaining a professional look.

Budget and Timeline:

We are looking for high-quality designs at a competitive price.
The project timeline is flexible, but we would appreciate prompt responses from designers.
Please submit your best pricing and estimated delivery times with your proposals.
We look forward to receiving your creative and professional designs that will represent Vostrana in the best possible light. Thank you for considering our project, and we can't wait to see your submissions on ArtHarbor!

Target Market(s)

Our primary target market for the corporate stationery design project includes, but is not limited to: Investors: Individuals or entities interested in commercial real estate investment opportunities. Brokers: Commercial real estate brokers who facilitate property transactions and negotiations. Tenant Representatives: Professionals who advocate for the interests of tenants in commercial lease transactions. Lenders: Financial institutions and lenders involved in providing financing for commercial real estate projects. Property Owners: Owners of commercial real estate properties seeking professional correspondence materials. Industry Partners: Professionals and organizations within the commercial real estate industry who collaborate with or provide services to Vostrana. Prospective Clients: Potential clients or partners exploring opportunities in the commercial real estate sector. Please note that while these are the primary target market segments, the stationery design should also appeal to a broader audience within the commercial real estate industry and convey professionalism and trustworthiness to all stakeholders.

Industry/Entity Type

Commercial Real Estate

Font styles to use
Sans Serif

Colors
0054AA
0677BA
7BADD7
CADEEF
E8F1F8
0094D4
00A9DD
6FCCEA
C7EBF8
E9F6FB
F0912C
F2A743
F7CA91
FBE8D2
FDF5EE
EE7325
F08F49
F5BC92
FAE3D3
FDF4ED

Requirements
Must have
• Brand Consistency: Ensure that the design adheres to Vostrana's existing brand standards and guidelines (provided in project attachments). Professional Appearance: The stationery must convey professionalism, trustworthiness, and excellence in the Commercial Real Estate industry. Logo Usage: Integrate the Vostrana logo prominently and appropriately on all stationery items. Contact Information: Include accurate contact details, such as the company's address, phone number, email address, and website URL. Typography: Use the specified fonts from the brand guidelines for all text elements, maintaining consistency in font style and size. Color Palette: Utilize the designated brand colors consistently throughout the design. File Formats: Ensure that the final design files are provided in high-resolution formats suitable for both print and digital use. Also, request editable source files (e.g., Adobe Illustrator, Photoshop) for future modifications if needed. Print-Ready: Prepare the design files to be print-ready, including the appropriate bleed and margin specifications for printing purposes. Stationery Variations: Include designs for letterhead, business cards, envelopes (multiple sizes if applicable), and general stationery. Creativity within Brand Guidelines: Encourage designers to be creative while working within the boundaries of Vostrana's brand standards, making the stationery unique and eye-catching. Versatility: Ensure that the stationery can be easily adapted for various purposes, such as formal business correspondence, presentations, and more. Timely Delivery: Specify your preferred timeline for receiving initial design concepts and revisions. Budget: Indicate your budget range for the project to attract designers who can provide high-quality work within your financial constraints. Responsive Designers: Request that designers are responsive to messages and able to make necessary revisions in a timely manner.
Nice to have
• Creative Elements: Incorporate unique and creative design elements that align with Vostrana's brand identity and the Commercial Real Estate industry. Texture or Embossing: If applicable and within budget, consider incorporating textured or embossed elements to add a tactile dimension to the stationery. Custom Illustrations: Include custom illustrations or graphics that convey the essence of the commercial real estate industry or your company's mission and values. Watermark or Background Pattern: Consider adding a subtle watermark or background pattern that complements the overall design without distracting from the content. Custom Typography: Explore the use of custom typography or stylized lettering for headers or key text elements to make the stationery more visually appealing. Enhanced Print Options: If budget allows, opt for premium printing techniques like foil stamping, spot UV, or letterpress to make the stationery truly stand out. Digital Templates: Request digital templates for electronic documents, such as Microsoft Word templates, PowerPoint templates, or PDF templates, to maintain consistency in digital communications. Multiple Design Concepts: Ask for variations of the stationery design to choose from, providing you with options for different occasions or purposes. QR Codes: If relevant, consider incorporating QR codes that link to Vostrana's website, portfolio, or contact information for convenient access. Environmentally Friendly Options: Explore eco-friendly printing materials and practices to align with sustainability goals, if applicable. Mobile Optimization: Ensure that any digital templates or elements are optimized for mobile use, enhancing accessibility and usability. Social Media Icons: Include social media icons and links to Vostrana's social media profiles, if desired, for a comprehensive online presence. Alternate Color Schemes: Request variations of the design with alternate color schemes for seasonal or special occasions.
Should not have
• Non-Compliance with Brand Guidelines: Specify that the design must strictly adhere to Vostrana's brand guidelines, and any deviations are not acceptable. Excessive Complexity: Avoid overly complex designs that may clutter the stationery or distract from the essential information. Inconsistent Branding: Ensure that all design elements, including colors, fonts, and logo usage, remain consistent with the provided brand standards. Unapproved Fonts: Specify that designers should only use the approved fonts from the brand guidelines and avoid introducing new fonts. Inappropriate Imagery: Request that designers refrain from using images, illustrations, or graphics that are unrelated to the Commercial Real Estate industry or that could potentially be perceived as unprofessional. Overly Bright Colors: If it doesn't align with your brand, discourage the use of overly bright or neon colors that may not convey professionalism. Clashing Color Schemes: Ensure that the color scheme chosen for the design is harmonious and avoids color combinations that clash or are difficult to read. Overuse of Effects: Discourage excessive use of visual effects, such as gradients, drop shadows, or excessive transparency, which can make the stationery appear cluttered. Extravagant Printing Costs: Specify that designers should consider budget constraints and avoid design elements that would significantly increase printing costs, unless the budget allows for premium printing techniques. Outdated Design Trends: Request that the design avoids incorporating outdated design trends that may make the stationery appear dated. Inconsistent Branding Across Items: Ensure that the design maintains consistency across all stationery items (letterhead, business cards, envelopes, etc.) and that there are no significant variations that could create confusion. Overly Busy Layouts: Ask for designs that have a clean and professional appearance, avoiding overcrowded layouts that make it difficult to read or find essential information.

```html
<!DOCTYPE html>
<html lang="en">
<head>
<meta charset="utf-8">
<title>Vostrana Business Card</title>
<link href="https://fonts.googleapis.com/css2?family=Montserrat:wght@300;400;700;800&display=swap" rel="stylesheet">
<style>
  :root {
    --backdrop: #3a3b3d;
    --navy: #0c2157;
    --navy-deep: #081a48;
    --brand-blue: #2f64b8;
    --sky-blue: #7badd7;
    --paper: #f6f6f4;
    --ink-soft: #6b6f78;
    --rule: #cfd2d8;
  }
  html, body {
    margin: 0;
    padding: 0;
    width: 1200px;
    height: 689px;
    overflow: hidden;
    background: var(--backdrop);
  }
  .canvas {
    position: relative;
    width: 1200px;
    height: 689px;
    font-family: "Montserrat", sans-serif;
  }
  .card {
    position: absolute;
    top: 195px;
    width: 520px;
    height: 300px;
    border-radius: 18px;
    overflow: hidden;
  }
  .card-back {
    left: 50px;
    background: var(--navy);
  }
  .back-pattern {
    position: absolute;
    inset: 0;
    background: linear-gradient(160deg, var(--navy) 0%, var(--navy-deep) 60%, #0f2a6a 100%);
  }
  .card-front {
    left: 630px;
    background: var(--paper);
  }
  .brand {
    position: absolute;
    left: 40px;
    top: 100px;
    width: 200px;
    display: flex;
    align-items: center;
    gap: 10px;
  }
  .brand-dot {
    width: 22px;
    height: 22px;
    border-radius: 50%;
    background: var(--brand-blue);
    flex: none;
  }
  .brand-name {
    font-weight: 800;
    font-size: 27px;
    letter-spacing: 3px;
    color: var(--navy);
  }
  .divider {
    position: absolute;
    left: 262px;
    top: 36px;
    width: 1px;
    height: 160px;
    background: var(--rule);
  }
  .contact {
    position: absolute;
    left: 284px;
    top: 34px;
    width: 220px;
    color: var(--ink-soft);
  }
  .person-name {
    margin: 0;
    font-weight: 700;
    font-size: 17px;
    color: var(--navy);
    letter-spacing: 0.3px;
  }
  .person-title {
    margin: 2px 0 12px;
    font-weight: 300;
    font-size: 11px;
  }
  .address {
    margin: 0 0 12px;
    font-style: normal;
    font-weight: 400;
    font-size: 11.5px;
    line-height: 1.45;
  }
  .details {
    list-style: none;
    margin: 0;
    padding: 0;
    font-size: 11.5px;
    line-height: 1.55;
  }
  .details li {
    display: flex;
    align-items: center;
    gap: 8px;
  }
  .details svg {
    width: 10px;
    height: 10px;
    fill: var(--navy);
    flex: none;
  }
  .skyline {
    position: absolute;
    left: 0;
    right: 0;
    bottom: 0;
    height: 48px;
    background: linear-gradient(180deg, var(--sky-blue) 0%, var(--brand-blue) 100%);
  }
</style>
</head>
<body>
<main class="canvas">
  <section class="card card-back" aria-label="Card reverse">
    <div class="back-pattern" role="img" aria-label="Embossed repeating pattern of tower outlines on navy"></div>
  </section>

  <section class="card card-front" aria-label="Card front">
    <div class="brand">
      <span class="brand-dot"></span>
      <span class="brand-name">VOSTRANA</span>
    </div>

    <div class="divider"></div>

    <div class="contact">
      <h1 class="person-name">DANIEL MOREAU</h1>
      <p class="person-title">Managing Director</p>
      <address class="address">4120 Linden Court<br>Harborview, Alaska 99512</address>
      <ul class="details">
        <li>
          <svg viewBox="0 0 10 10"><path d="M2 0.5 L3.6 0.5 L4.2 2.8 L3 3.6 Q4 5.8 6.4 7 L7.2 5.8 L9.5 6.4 L9.5 8 Q9.5 9.5 8 9.5 Q0.5 9 0.5 2 Q0.5 0.5 2 0.5Z"/></svg>
          555-210-4817
        </li>
        <li>
          <svg viewBox="0 0 10 10"><path d="M2.5 0 H7.5 Q8.3 0 8.3 0.8 V9.2 Q8.3 10 7.5 10 H2.5 Q1.7 10 1.7 9.2 V0.8 Q1.7 0 2.5 0Z M2.8 1.2 V8 H7.2 V1.2Z"/></svg>
          555-362-9045
        </li>
        <li>
          <svg viewBox="0 0 10 10"><path d="M0 2 H10 V8.5 H0Z M0.8 2.6 L5 5.6 L9.2 2.6 V3.4 L5 6.4 L0.8 3.4Z" fill-rule="evenodd"/></svg>
          info@vostrana.com
        </li>
        <li>
          <svg viewBox="0 0 10 10"><circle cx="5" cy="5" r="4.6"/></svg>
          www.vostrana.com
        </li>
      </ul>
    </div>

    <div class="skyline" role="img" aria-label="Row of blue city tower shapes along the bottom edge"></div>
  </section>
</main>
</body>
</html>
```